KVRD Pinecrest Rehabilitation Consultants, INC
Business Card and Stationary for KVRD Pinecrest Rehabilitation
Professional
Dorian K. Lumbard, Ph. D.
Vocational Rehabilitation Consultant
4173b GA Hwy 508 STE 612 Conyers, GA 30081
Dorian.Lumbard@kvrdpinecrestrehab.example
www.kvrdpinecrestrehab.example
I will need whole set of stationary, letterhead, envelopes etc.

```html
<!DOCTYPE html>
<html lang="en">
<head>
<meta charset="utf-8">
<title>KVRD Pinecrest Rehabilitation – Business Card</title>
<link href="https://fonts.googleapis.com/css2?family=Cinzel:wght@500&family=Oswald:wght@500&family=Open+Sans:wght@400&display=swap" rel="stylesheet">
<style>
  :root{
    --bg:#d6d6d6;
    --card:#ffffff;
    --blue:#3a6cb4;
    --ink:#2f2f33;
    --grey:#6d6f74;
  }
  *{box-sizing:border-box;margin:0;padding:0}
  html,body{width:1200px;height:949px;overflow:hidden;background:var(--bg)}
  .canvas{position:relative;width:1200px;height:949px}
  .card{position:absolute;left:290px;width:620px;height:354px;background:var(--card);border-radius:16px;box-shadow:0 6px 18px rgba(0,0,0,.18)}
  .card--back{top:60px}
  .card--front{top:480px}

  /* brand wordmark: one colour, one weight */
  .wordmark{font:500 22px/1.3 'Cinzel',serif;color:var(--blue);letter-spacing:1.5px}
  .wordmark__dot{display:block;width:22px;height:22px;border-radius:50%;background:var(--blue);margin-bottom:12px}

  /* back */
  .back-brand{position:absolute;left:0;right:0;top:120px;display:flex;flex-direction:column;align-items:center;text-align:center}
  .back-brand .wordmark__dot{margin-bottom:14px}
  .social{position:absolute;right:30px;bottom:26px;display:flex;gap:22px;font:400 12px 'Open Sans',sans-serif;color:var(--grey)}
  .social__item{display:flex;align-items:center;gap:6px}
  .social__box{width:14px;height:14px;background:var(--blue);border-radius:2px}

  /* front */
  .brand{position:absolute;left:34px;top:0;bottom:0;width:200px;display:flex;flex-direction:column;justify-content:center}

  .identity{position:absolute;left:262px;top:40px;border-left:3px solid var(--ink);padding-left:14px}
  .identity__name{font:500 24px 'Oswald',sans-serif;color:var(--blue);letter-spacing:1px;text-transform:uppercase;line-height:1.15}
  .identity__title{font:400 13px 'Open Sans',sans-serif;color:var(--grey);margin-top:4px}

  .contacts{position:absolute;left:262px;top:140px;display:flex;flex-direction:column;gap:20px}
  .contact{display:flex;align-items:center;gap:12px}
  .contact__icon{width:26px;height:26px;flex:none}
  .contact__text{border-left:3px solid var(--ink);padding-left:10px;font:400 12px/1.5 'Open Sans',sans-serif;color:var(--ink);white-space:nowrap}
</style>
</head>
<body>
<div class="canvas">

  <section class="card card--back">
    <div class="back-brand">
      <span class="wordmark__dot"></span>
      <div class="wordmark">KVRD Pinecrest<br>Rehabilitation</div>
    </div>
    <div class="social">
      <div class="social__item"><span class="social__box"></span>/kvrdpinecrest</div>
      <div class="social__item"><span class="social__box"></span>/kvrdpinecrestrehab</div>
    </div>
  </section>

  <section class="card card--front">
    <div class="brand">
      <span class="wordmark__dot"></span>
      <div class="wordmark">KVRD Pinecrest<br>Rehabilitation</div>
    </div>

    <div class="identity">
      <div class="identity__name">Dorian K. Lumbard, Ph. D.</div>
      <div class="identity__title">Vocational Rehabilitation Consultant</div>
    </div>

    <div class="contacts">
      <div class="contact">
        <svg class="contact__icon" viewBox="0 0 30 30" aria-hidden="true">
          <path d="M15 2 C8 2 4 7 4 12 C4 19 15 28 15 28 C15 28 26 19 26 12 C26 7 22 2 15 2 Z" fill="var(--blue)"/>
          <circle cx="15" cy="12" r="4" fill="#fff"/>
        </svg>
        <div class="contact__text">4173b GA Hwy 508 STE 612<br>Conyers, GA 30081</div>
      </div>
      <div class="contact">
        <svg class="contact__icon" viewBox="0 0 30 30" aria-hidden="true">
          <path d="M8 3 L12 3 L14 9 L11 11 Q13 17 19 19 L21 16 L27 18 L27 22 Q27 27 22 27 Q5 25 3 8 Q3 3 8 3 Z" fill="var(--blue)"/>
        </svg>
        <div class="contact__text">012 555 0148<br>Dorian.Lumbard@kvrdpinecrestrehab.example</div>
      </div>
      <div class="contact">
        <svg class="contact__icon" viewBox="0 0 30 30" aria-hidden="true">
          <circle cx="15" cy="15" r="12" fill="none" stroke="var(--blue)" stroke-width="2.4"/>
          <ellipse cx="15" cy="15" rx="5" ry="12" fill="none" stroke="var(--blue)" stroke-width="2"/>
          <line x1="3" y1="15" x2="27" y2="15" stroke="var(--blue)" stroke-width="2"/>
          <line x1="5" y1="9" x2="25" y2="9" stroke="var(--blue)" stroke-width="1.6"/>
          <line x1="5" y1="21" x2="25" y2="21" stroke="var(--blue)" stroke-width="1.6"/>
        </svg>
        <div class="contact__text">www.kvrdpinecrestrehab.example</div>
      </div>
    </div>
  </section>

</div>
</body>
</html>
```